KESTREL Communications Business Card- Belsa

Kestrel Integrated Communications is Corporate communications agency with more than 20 years of experience. We become part of the manegement team of our clients in other to improve their outcomes and grow the possitioning of their brand.
We are in Puerto Rico, latin caribbean island
Name: Maribelsa (Belsa) Ocampo
787-555-0148
bocampo@kestrelwing.example

Target Market(s)

finance and pharmaceutical companies

Industry/Entity Type

Business

Contact Information for Business Card

modern, edgy colorful and playfull like our logo

Requirements
Must have
• company logo
• name
• tel
• email

```html
<!DOCTYPE html>
<html lang="en">
<head>
<meta charset="utf-8">
<title>Kestrel Integrated Communications — Business Card</title>
<link rel="stylesheet" href="https://fonts.googleapis.com/css2?family=Open+Sans:wght@400;600&display=swap">
<style>
  :root {
    --bg: #ece9e4;
    --card-white: #fbfbfb;
    --orange: #e8702a;
    --orange-deep: #d95f1c;
    --orange-soft: #f39a4c;
    --brown: #5a3a12;
    --map-tint: #f6e4dc;
    --white: #ffffff;
  }
  * { box-sizing: border-box; margin: 0; padding: 0; }
  html, body {
    width: 1200px; height: 1023px; overflow: hidden;
    background: var(--bg);
    font-family: "Open Sans", Arial, sans-serif;
  }
  .stage {
    width: 1200px; height: 1023px;
    display: flex; flex-direction: column; align-items: center; justify-content: center;
    gap: 60px;
  }
  .card {
    width: 630px; height: 360px; position: relative; overflow: hidden;
    box-shadow: 0 6px 18px rgba(0,0,0,.18);
  }
  /* Front */
  .card-front { background: var(--card-white); }
  .world-map {
    position: absolute; left: 150px; top: 60px; width: 330px; height: 170px;
    background: radial-gradient(ellipse at center, var(--map-tint) 0%, rgba(246,228,220,0) 70%);
  }
  .brand {
    position: absolute; left: 0; right: 0; top: 92px;
    display: flex; flex-direction: column; align-items: center; gap: 10px;
  }
  .brand-row { display: flex; align-items: center; gap: 14px; }
  .brand-dot { width: 22px; height: 22px; border-radius: 50%; background: var(--orange); }
  .brand-name {
    font-weight: 600; font-size: 58px; letter-spacing: 6px; color: var(--brown); line-height: 1;
  }
  .brand-tagline {
    font-weight: 600; font-size: 14px; letter-spacing: 3px; color: var(--brown); text-transform: uppercase;
  }
  .band {
    position: absolute; left: 0; right: 0; bottom: 0; height: 86px;
    background: var(--orange);
    display: flex; align-items: center; justify-content: center;
  }
  .band-rules {
    position: absolute; left: 0; right: 0; top: 6px; height: 8px;
    border-top: 2px solid var(--white); border-bottom: 2px solid var(--white);
  }
  .website {
    margin-top: 14px;
    color: var(--white); font-weight: 600; font-size: 16px; letter-spacing: 3px;
  }
  /* Back */
  .card-back {
    background: linear-gradient(135deg, var(--orange-soft) 0%, var(--orange) 55%, var(--orange-deep) 100%);
    padding: 70px 56px;
  }
  .person-name { font-weight: 600; font-size: 28px; color: var(--brown); }
  .person-title { font-size: 14px; color: var(--brown); margin-top: 4px; letter-spacing: 1px; }
  .contact { position: absolute; left: 56px; bottom: 60px; color: var(--brown); font-size: 15px; line-height: 1.8; }
  .contact-row { display: flex; align-items: center; gap: 10px; }
  .contact-row svg { width: 14px; height: 14px; fill: var(--brown); }
</style>
</head>
<body>
<main class="stage">
  <section class="card card-front">
    <div class="world-map" role="img" aria-label="Faint dotted world map"></div>
    <div class="brand">
      <div class="brand-row">
        <span class="brand-dot"></span>
        <span class="brand-name">KESTREL</span>
      </div>
      <span class="brand-tagline">Integrated Communications</span>
    </div>
    <div class="band">
      <div class="band-rules"></div>
      <span class="website">www.kestrelwing.example</span>
    </div>
  </section>

  <section class="card card-back">
    <h1 class="person-name">Maribelsa (Belsa) Ocampo</h1>
    <p class="person-title">Account Director</p>
    <div class="contact">
      <div class="contact-row">
        <svg viewBox="0 0 24 24"><path d="M6.6 10.8a15.1 15.1 0 0 0 6.6 6.6l2.2-2.2c.3-.3.7-.4 1-.2 1.1.4 2.3.6 3.6.6.6 0 1 .4 1 1V20c0 .6-.4 1-1 1A17 17 0 0 1 3 4c0-.6.4-1 1-1h3.5c.6 0 1 .4 1 1 0 1.3.2 2.5.6 3.6.1.3 0 .7-.2 1z"/></svg>
        <span>787-555-0148</span>
      </div>
      <div class="contact-row">
        <svg viewBox="0 0 24 24"><path d="M2 5h20v14H2zm2 2v.5l8 5 8-5V7zm0 2.8V17h16V9.8l-8 5z"/></svg>
        <span>bocampo@kestrelwing.example</span>
      </div>
    </div>
  </section>
</main>
</body>
</html>
```